Luxury WordPress Website for CORALBASINS

I need a professional WordPress website for Coral Basins. The site should be modern, visually appealing, and user-friendly, reflecting the brand’s luxury and premium identity. It must include a homepage, product/service pages, contact form, and be responsive on both desktop and mobile devices. The design should allow for easy updates and integration of future content, while maintaining a polished and professional look.

Target Market(s)

swimmingpool & spa

Industry/Entity Type

Swimmingpool

Coding

Coded - Design and coding required

Font styles to use
Other font styles liked:
• HaboroSoft

Requirements
Must have
• Exclusive appearance
Nice to have
• • A logo that subtly incorporates water or pool elements. • A color palette that reflects luxury, elegance, and relaxation. • Clean and modern typography that is easy to read across all media. • Iconography or design elements that convey premium quality. • A versatile design that can be adapted for social media, merchandise, and promotional materials. • Optional: A tagline that emphasizes luxury and high-end pool experiences.

```html
<!DOCTYPE html>
<html lang="en">
<head>
<meta charset="UTF-8">
<title>Coral Basins — Luxury Pools</title>
<link href="https://fonts.googleapis.com/css2?family=Saira+Semi+Condensed:wght@400;600;700&family=Lato:wght@400;700&display=swap" rel="stylesheet">
<style>
:root{
  --blue:#1652ae;
  --blue-dark:#1249a0;
  --blue-soft:#e7f0fa;
  --sky:#5ba3de;
  --water:#2a8fd6;
  --ink:#1c1c1c;
  --text:#444;
  --white:#fff;
  --teal:#1fb7c4;
}
*{box-sizing:border-box;margin:0;padding:0}
html,body{width:1200px;height:3970px;overflow:hidden}
body{font-family:"Lato",sans-serif;color:var(--ink);background:var(--white);position:relative}
.abs{position:absolute}
.heading{font-family:"Saira Semi Condensed",sans-serif;font-weight:400;color:var(--ink);text-align:center;font-size:42px;line-height:1}
.heading b{color:var(--blue);font-weight:700}
.squiggle{display:block;margin:10px auto 0}
.btn{position:absolute;display:flex;align-items:center;justify-content:center;background:var(--blue);color:var(--white);font-weight:700;font-size:17px;border-radius:24px}
.photo{position:absolute}

/* header */
.site-header{top:0;left:0;width:1200px;height:94px;background:var(--white)}
.brand{display:flex;align-items:center;gap:12px}
.brand-dot{width:58px;height:58px;border-radius:50%;background:var(--blue)}
.brand-name{font-weight:700;font-size:24px;letter-spacing:2px;line-height:1.05;color:var(--ink)}
.brand-name span{display:block;font-size:17px;letter-spacing:6px;padding-left:30px}
.nav{display:flex;gap:34px;font-size:15px;top:36px;left:660px}

/* hero */
.hero{top:94px;left:0;width:1200px;height:600px}
.hero h1{font-family:"Saira Semi Condensed",sans-serif;font-weight:600;color:var(--white);font-size:52px;line-height:1.2;left:110px;top:100px;text-shadow:0 2px 6px rgba(0,0,0,.3)}
.hero p{left:110px;top:240px;width:440px;color:var(--white);font-weight:700;font-size:17px;line-height:1.5}

/* services */
.service-card{position:absolute;top:847px;width:306px;height:346px;background:var(--white);border-radius:0 0 0 40px;box-shadow:0 3px 8px rgba(0,0,0,.15);overflow:hidden}
.service-card .photo{top:0;left:0;width:306px;height:266px}
.service-icon{position:absolute;left:16px;top:220px;width:68px;height:68px;border-radius:50%;background:var(--blue);border:3px solid var(--white);display:flex;align-items:center;justify-content:center}
.service-card h3{position:absolute;top:294px;left:0;width:306px;text-align:center;font-family:"Saira Semi Condensed",sans-serif;font-weight:400;font-size:21px}
.arrow{position:absolute;width:30px;height:30px}

/* about */
.about{top:1280px;left:0;width:1200px;height:565px;background:var(--blue-soft)}
.about-frame{left:110px;top:80px;width:450px;height:395px;border:6px solid var(--blue);border-radius:0 50px 0 50px;overflow:hidden}
.about-text{left:642px;top:470px}
.about p{position:absolute;left:642px;top:172px;width:446px;font-size:14px;line-height:1.85;color:var(--text);text-align:justify}

/* projects */
.project{position:absolute;box-shadow:0 2px 6px rgba(0,0,0,.12)}

/* cta */
.cta{top:2613px;left:0;width:1200px;height:397px;background:linear-gradient(180deg,#2a6cc4 0%,#1d5bb5 60%,#2a66bf 100%)}
.cta .heading{color:var(--white);position:absolute;top:100px;width:1200px}
.cta .heading b{color:var(--white)}
.cta p{position:absolute;top:185px;left:230px;width:740px;text-align:center;color:var(--white);font-weight:700;font-size:17px;line-height:1.55}
.cta .btn{background:var(--white);color:var(--ink);top:265px;left:464px;width:272px;height:46px}

/* testimonials */
.quote-card{position:absolute;top:3205px;width:310px;height:245px;background:var(--white);border-radius:0 0 40px 40px;box-shadow:0 3px 8px rgba(0,0,0,.15)}
.quote-mark{position:absolute;top:-14px;left:24px;font-family:"Saira Semi Condensed",sans-serif;font-weight:700;font-size:70px;line-height:1;color:var(--blue)}
.quote-card p{position:absolute;top:36px;left:24px;width:270px;font-size:14px;line-height:1.9;color:var(--text)}
.avatar{position:absolute;left:24px;top:155px;width:68px;height:68px;border-radius:50%;background:linear-gradient(#cfd6de,#9aa6b3)}
.client{position:absolute;left:114px;top:170px}
.client strong{display:block;font-size:19px;font-weight:700}
.client span{font-size:14px;color:var(--text)}

/* footer */
.site-footer{top:3537px;left:0;width:1200px;height:433px;background:var(--blue-dark);color:var(--white)}
.site-footer .brand-name{color:var(--white)}
.site-footer .brand-dot{background:var(--white)}
.foot-col h4{font-size:19px;font-weight:700;margin-bottom:22px}
.foot-col ul{list-style:none}
.foot-col li{font-size:14px;margin-bottom:17px;padding-left:22px;position:relative}
.foot-col li::before{content:"";position:absolute;left:0;top:6px;width:7px;height:7px;border-radius:50%;background:var(--white)}
.contact-line{display:flex;gap:10px;font-size:14px;line-height:1.6;margin-bottom:18px}
.social{display:flex;gap:14px}
.social i{width:22px;height:22px;border-radius:50%;background:var(--white);display:block}
.email-box{left:110px;top:248px;width:220px;height:42px;background:var(--white);color:#555;font-size:14px;padding:14px 22px}
.subscribe{left:110px;top:304px;width:118px;height:42px;background:var(--teal);font-weight:700;font-size:16px;display:flex;align-items:center;justify-content:center}
.foot-rule{left:110px;top:382px;width:980px;height:1px;background:rgba(255,255,255,.4)}
.copyright{top:402px;left:0;width:1200px;text-align:center;font-size:14px}
</style>
</head>
<body>

<header class="site-header abs">
  <div class="brand abs" style="left:110px;top:14px">
    <div class="brand-dot"></div>
    <div class="brand-name">CORAL<span>BASINS</span></div>
  </div>
  <nav class="nav abs"><span>Home</span><span>Projects</span><span>Contact Us</span></nav>
  <div class="btn" style="left:938px;top:22px;width:150px;height:46px">Get a Quote</div>
</header>

<section class="hero abs">
  <svg class="abs" width="1200" height="600" style="top:0;left:0" role="img" aria-label="Infinity pool terrace with loungers, parasols and palm trees under a bright sky">
    <defs>
      <linearGradient id="heroSky" x1="0" y1="0" x2="0" y2="1">
        <stop offset="0" stop-color="#3a86d4"/>
        <stop offset=".35" stop-color="#8ec0ea"/>
        <stop offset=".5" stop-color="#3c8fd8"/>
        <stop offset="1" stop-color="#0f5fb8"/>
      </linearGradient>
    </defs>
    <path d="M0 0H1200V575C1050 610 900 540 700 545C520 550 420 620 250 590C150 575 60 560 0 590Z" fill="url(#heroSky)"/>
    <path d="M0 590C60 560 150 575 250 590C420 620 520 550 700 545C900 540 1050 610 1200 575V600H0Z" fill="#fff"/>
  </svg>
  <h1 class="abs">Crafted for Those Who<br>Demand the Extraordinary</h1>
  <p class="abs">Coral Basins brings artistry, precision, and timeless design to your private oasis.</p>
  <div class="btn" style="left:110px;top:318px;width:150px;height:46px">Get Started</div>
</section>

<section>
  <div class="abs" style="top:752px;left:0;width:1200px">
    <h2 class="heading">Our <b>Services</b></h2>
    <svg class="squiggle" width="100" height="14"><path d="M4 8C30 14 60 2 96 6" stroke="#1652ae" stroke-width="4" fill="none" stroke-linecap="round"/></svg>
  </div>

  <svg class="arrow" style="left:38px;top:1006px" viewBox="0 0 30 30"><circle cx="15" cy="15" r="13" fill="none" stroke="#1652ae" stroke-width="2"/><path d="M20 15H10M14 10L9 15L14 20" stroke="#1652ae" stroke-width="2" fill="none"/></svg>
  <svg class="arrow" style="left:1134px;top:1006px" viewBox="0 0 30 30"><circle cx="15" cy="15" r="13" fill="none" stroke="#888" stroke-width="2"/><path d="M10 15H20M16 10L21 15L16 20" stroke="#888" stroke-width="2" fill="none"/></svg>

  <article class="service-card" style="left:110px">
    <div class="photo" role="img" aria-label="Modern villa with pool at sunset" style="background:linear-gradient(180deg,#e89a4e 0%,#c98a5c 40%,#6a9fc4 75%,#9cc8de 100%)"></div>
    <div class="service-icon"><svg width="34" height="34" viewBox="0 0 34 34"><circle cx="17" cy="17" r="8" fill="none" stroke="#fff" stroke-width="2.5"/><circle cx="17" cy="17" r="3" fill="#fff"/><path d="M17 3V9M17 25V31M3 17H9M25 17H31" stroke="#fff" stroke-width="2.5"/></svg></div>
    <h3>Bespoke Pool Design</h3>
  </article>
  <article class="service-card" style="left:447px">
    <div class="photo" role="img" aria-label="Freeform pool with stone waterfall" style="background:linear-gradient(180deg,#4a6b3c 0%,#5f7e56 35%,#2b7fb8 60%,#1f6fab 85%,#c7b9a4 100%)"></div>
    <div class="service-icon"><svg width="34" height="34" viewBox="0 0 34 34"><path d="M6 24C10 20 14 28 18 24S26 20 29 24" stroke="#fff" stroke-width="2.5" fill="none"/><rect x="10" y="7" width="14" height="10" rx="2" fill="#fff"/></svg></div>
    <h3>Luxury Pool Construction</h3>
  </article>
  <article class="service-card" style="left:783px">
    <div class="photo" role="img" aria-label="Renovated backyard pool with outdoor fireplace" style="background:linear-gradient(180deg,#9cc4e4 0%,#597c4a 35%,#6e8c5a 55%,#2a8fcf 75%,#9aa3a8 100%)"></div>
    <div class="service-icon"><svg width="34" height="34" viewBox="0 0 34 34"><path d="M7 27L22 12M12 7L27 22" stroke="#fff" stroke-width="4" stroke-linecap="round"/></svg></div>
    <h3>Renovation &amp; Modernization</h3>
  </article>
</section>

<section class="about abs">
  <div class="about-frame abs"><div role="img" aria-label="Pool builder reviewing plans beside a finished pool" style="width:100%;height:100%;background:linear-gradient(180deg,#5d9fe0 0%,#b6d6ef 45%,#3aa2d6 70%,#1e86c2 100%)"></div></div>
  <div class="abs" style="left:642px;top:80px">
    <h2 class="heading" style="text-align:left">About <b>Coral Basins</b></h2>
    <svg class="squiggle" style="margin-left:0" width="100" height="14"><path d="M4 8C30 14 60 2 96 6" stroke="#1652ae" stroke-width="4" fill="none" stroke-linecap="round"/></svg>
  </div>
  <p>At Coral Basins, we believe that a pool is more than a feature — it's a statement of lifestyle, artistry, and timeless design. Each project we create is a masterpiece of craftsmanship and innovation, blending the tranquility of water with the sophistication of modern architecture. For those who seek perfection, our work represents the pinnacle of precision and beauty. From the first sketch to the final tile, every detail is meticulously curated to reflect your vision, environment, and personality.</p>
  <div class="btn" style="left:642px;top:433px;width:152px;height:45px">Read More</div>
</section>

<section>
  <div class="abs" style="top:1924px;left:0;width:1200px">
    <h2 class="heading">Featured <b>projects</b></h2>
    <svg class="squiggle" width="100" height="14"><path d="M4 8C30 14 60 2 96 6" stroke="#1652ae" stroke-width="4" fill="none" stroke-linecap="round"/></svg>
  </div>
  <div class="project" role="img" aria-label="Rooftop infinity pool under cloudy sky" style="left:110px;top:2018px;width:359px;height:414px;background:linear-gradient(180deg,#3f86d6 0%,#cfe2f3 35%,#7cc0e6 55%,#2a9ad8 100%)"></div>
  <div class="project" role="img" aria-label="Evening pool with fire pit" style="left:485px;top:2018px;width:192px;height:199px;background:linear-gradient(180deg,#7d8f9c 0%,#6e5a42 45%,#1f5f9a 75%,#14416e 100%)"></div>
  <div class="project" role="img" aria-label="Mediterranean villa pool" style="left:691px;top:2018px;width:192px;height:199px;background:linear-gradient(180deg,#2a78d0 0%,#d8b98c 45%,#30c0d6 75%,#1aa5c9 100%)"></div>
  <div class="project" role="img" aria-label="Builder holding plans by a pool" style="left:897px;top:2018px;width:192px;height:199px;background:linear-gradient(180deg,#8e8274 0%,#b7aea3 45%,#4aa6d4 75%,#2b8fcb 100%)"></div>
  <div class="project" role="img" aria-label="Modern home with turquoise pool" style="left:485px;top:2233px;width:192px;height:199px;background:linear-gradient(180deg,#6fa9de 0%,#a48a6e 40%,#35bcd4 70%,#d8cdbb 100%)"></div>
  <div class="project" role="img" aria-label="Garden pool with waterfall" style="left:691px;top:2233px;width:192px;height:199px;background:linear-gradient(180deg,#9fc5e6 0%,#4e6d3e 40%,#2b7fc0 70%,#c2b8a6 100%)"></div>
  <div class="project" role="img" aria-label="Covered patio beside deep blue pool" style="left:897px;top:2233px;width:192px;height:199px;background:linear-gradient(180deg,#d8dde2 0%,#7c8f6e 40%,#2462c2 70%,#1b4fa8 100%)"></div>
  <div class="btn" style="left:526px;top:2482px;width:150px;height:46px">View More</div>
</section>

<section class="cta abs" role="img" aria-label="Blue-tinted backdrop of pool plans and drafting tools">
  <h2 class="heading">Transform Your <b>Backyard Into a Private Paradise</b></h2>
  <svg class="abs" style="left:550px;top:140px" width="100" height="14"><path d="M4 8C30 14 60 2 96 6" stroke="#fff" stroke-width="4" fill="none" stroke-linecap="round"/></svg>
  <p>Discover the ultimate in luxury pool design. From custom layouts to exquisite materials, we create pools that are more than just water—they're a lifestyle.</p>
  <div class="btn">Schedule Your Consultation</div>
</section>

<section>
  <div class="abs" style="top:3090px;left:0;width:1200px">
    <h2 class="heading">What Our <b>Clients Say</b></h2>
    <svg class="squiggle" width="100" height="14"><path d="M4 8C30 14 60 2 96 6" stroke="#1652ae" stroke-width="4" fill="none" stroke-linecap="round"/></svg>
  </div>
  <svg class="arrow" style="left:38px;top:3306px" viewBox="0 0 30 30"><circle cx="15" cy="15" r="13" fill="none" stroke="#1652ae" stroke-width="2"/><path d="M20 15H10M14 10L9 15L14 20" stroke="#1652ae" stroke-width="2" fill="none"/></svg>
  <svg class="arrow" style="left:1134px;top:3306px" viewBox="0 0 30 30"><circle cx="15" cy="15" r="13" fill="none" stroke="#888" stroke-width="2"/><path d="M10 15H20M16 10L21 15L16 20" stroke="#888" stroke-width="2" fill="none"/></svg>

  <article class="quote-card" style="left:110px">
    <div class="quote-mark">“</div>
    <p>Coral Basins transformed our backyard into a serene oasis. The craftsmanship and attention to detail are unmatched – truly a masterpiece.</p>
    <div class="avatar" role="img" aria-label="Client portrait"></div>
    <div class="client"><strong>Marcus T.</strong><span>Beverly Hills</span></div>
  </article>
  <article class="quote-card" style="left:445px">
    <div class="quote-mark">“</div>
    <p>From design to installation, the team made the entire process effortless. Our infinity pool is now the centerpiece of our home.</p>
    <div class="avatar" role="img" aria-label="Client portrait"></div>
    <div class="client"><strong>Elena V.,</strong><span>Miami</span></div>
  </article>
  <article class="quote-card" style="left:780px">
    <div class="quote-mark">“</div>
    <p>Professional, punctual, and innovative. We feel like we've brought a five-star resort into our private residence. Every aspect of our pool screams luxury.</p>
    <div class="avatar" role="img" aria-label="Client portrait"></div>
    <div class="client"><strong>Julian K.,</strong><span>Dubai</span></div>
  </article>
</section>

<footer class="site-footer abs">
  <div class="brand abs" style="left:110px;top:72px">
    <div class="brand-dot"></div>
    <div class="brand-name">CORAL<span>BASINS</span></div>
  </div>
  <div class="social abs" style="left:112px;top:190px"><i></i><i></i><i></i><i></i></div>
  <div class="email-box abs">Email</div>
  <div class="subscribe abs">Subscribe</div>

  <div class="foot-col abs" style="left:436px;top:78px">
    <h4>Quick Links</h4>
    <ul><li>Home</li><li>About Us</li><li>Products / Services</li><li>Gallery</li><li>Blog</li></ul>
  </div>
  <div class="foot-col abs" style="left:646px;top:78px">
    <h4>Locations</h4>
    <ul><li>San Diego (HQ)</li><li>Boston</li><li>Miami</li><li>Seattle</li><li>DC</li></ul>
  </div>
  <div class="foot-col abs" style="left:883px;top:78px">
    <h4>Contact Us</h4>
    <div class="contact-line"><svg width="18" height="18" viewBox="0 0 18 18"><path d="M9 1C5.5 1 3 3.6 3 7C3 11 9 17 9 17S15 11 15 7C15 3.6 12.5 1 9 1Z" fill="#fff"/><circle cx="9" cy="7" r="2.3" fill="#1249a0"/></svg><span>Harbor Row. 82 W Tide Ave,<br>New York, NY 10014,</span></div>
    <div class="contact-line"><svg width="18" height="18" viewBox="0 0 18 18"><circle cx="9" cy="9" r="8" fill="#fff"/><rect x="4.5" y="6" width="9" height="6" fill="none" stroke="#1249a0" stroke-width="1.3"/><path d="M4.5 6L9 9.5L13.5 6" stroke="#1249a0" stroke-width="1.3" fill="none"/></svg><span>info@coralbasins.com</span></div>
    <div class="contact-line"><svg width="18" height="18" viewBox="0 0 18 18"><circle cx="9" cy="9" r="8" fill="#fff"/><path d="M6 5L7.5 5L8.3 7.3L7.3 8.2C7.8 9.3 8.7 10.2 9.8 10.7L10.7 9.7L13 10.5V12C13 12.6 12.5 13 12 13C8.7 12.8 5.2 9.3 5 6C5 5.5 5.4 5 6 5Z" fill="#1249a0"/></svg><span>+1 555 010 2040</span></div>
  </div>

  <div class="foot-rule abs"></div>
  <div class="copyright abs">© 2025 Coral Basins. All rights reserved.</div>
</footer>

</body>
</html>
```